Create Lanternfield HR Business Cards.

Create Business Cards for Lanternfield HR. 2 sided and Would like the back to have the logo.

Info for Business Card:
Address: 4827 Millbrook Ave Suite 230 Cleveland, Ohio 44987
Office Number: 216-555-0143
Mobile: 216-555-0192

Website: www.lanternfieldhr.example

Target Market(s)

Small to medium size businesses

Industry/Entity Type

Human Resources

Contact Information for Business Card

Company logo and information

Font styles to use
Serif
Sans Serif

Requirements
Must have
• Info for Business Card: Address: 4827 Millbrook Ave Suite 230 Cleveland, Ohio 44987 Office Number: 216-555-0143 Mobile: 216-555-0192 Website: www.lanternfieldhr.example

```html
<!DOCTYPE html>
<html lang="en">
<head>
<meta charset="utf-8">
<title>Lanternfield HR Business Cards</title>
<link href="https://fonts.googleapis.com/css2?family=Montserrat:wght@500;600;800&family=Nunito+Sans:wght@500;600&display=swap" rel="stylesheet">
<style>
  :root{
    --navy:#241f63;
    --orange:#ff8300;
    --white:#ffffff;
    --backdrop:#2a2a2c;
  }
  *{box-sizing:border-box;margin:0;padding:0}
  html,body{width:1200px;height:1200px;overflow:hidden;background:var(--backdrop)}
  .stage{position:relative;width:1200px;height:1200px}
  .card{position:absolute;top:215px;width:440px;height:770px;border-radius:26px;overflow:hidden;background:var(--navy)}
  .card--front{left:110px}
  .card--back{left:650px}

  /* front */
  .front-mark{position:absolute;left:0;right:0;top:300px;display:flex;justify-content:center}
  .front-name{font-family:"Montserrat",sans-serif;font-weight:800;color:var(--white);font-size:52px;line-height:1.1;text-align:center;letter-spacing:.5px}

  /* back */
  .back-bg{position:absolute;inset:0}
  .back-mark{position:absolute;left:0;right:0;top:215px;display:flex;justify-content:center}
  .back-name{font-family:"Montserrat",sans-serif;font-weight:800;color:var(--navy);font-size:38px;line-height:1.1;text-align:center}

  .details{position:absolute;left:0;right:0;top:490px;text-align:center;color:var(--white);font-family:"Montserrat",sans-serif}
  .person{font-weight:800;font-size:24px;letter-spacing:.3px;text-transform:uppercase}
  .role{font-weight:500;font-size:17px;margin-top:4px}
  .icons{display:flex;justify-content:center;gap:26px;margin:16px 0 12px}
  .icon{width:30px;height:30px;border-radius:50%;background:var(--white);display:flex;align-items:center;justify-content:center}
  .icon svg{width:18px;height:18px}
  .contact{font-weight:600;font-size:15px;line-height:1.55}
  .rule{width:230px;height:1px;background:var(--white);margin:16px auto 14px}
  .address{font-family:"Nunito Sans",sans-serif;font-weight:600;font-size:16px;line-height:1.5;letter-spacing:.8px}
</style>
</head>
<body>
<main class="stage">

  <section class="card card--front" aria-label="Card front">
    <div class="front-mark">
      <h1 class="front-name">Lanternfield<br>HR</h1>
    </div>
  </section>

  <section class="card card--back" aria-label="Card back">
    <svg class="back-bg" viewBox="0 0 440 770" preserveAspectRatio="none" aria-hidden="true">
      <rect width="440" height="770" fill="var(--navy)"/>
      <rect width="440" height="300" fill="var(--white)"/>
      <rect y="300" width="440" height="10" fill="var(--orange)"/>
      <circle cx="220" cy="290" r="178" fill="var(--white)"/>
    </svg>

    <div class="back-mark">
      <p class="back-name">Lanternfield<br>HR</p>
    </div>

    <div class="details">
      <p class="person">Daniel Whitmore</p>
      <p class="role">Co-Founder &amp; CEO</p>
      <div class="icons">
        <span class="icon"><svg viewBox="0 0 24 24" fill="none" stroke="var(--orange)" stroke-width="2"><rect x="7" y="2" width="10" height="20" rx="2"/><line x1="11" y1="18" x2="13" y2="18"/></svg></span>
        <span class="icon"><svg viewBox="0 0 24 24" fill="var(--orange)"><path d="M3 9c0-3 4-5 9-5s9 2 9 5v2h-5V9H8v2H3z"/><path d="M6 12h12l2 8H4z"/></svg></span>
        <span class="icon"><svg viewBox="0 0 24 24" fill="none" stroke="var(--orange)" stroke-width="2"><rect x="3" y="6" width="18" height="12" rx="1"/><path d="M3 7l9 6 9-6"/></svg></span>
        <span class="icon"><svg viewBox="0 0 24 24" fill="none" stroke="var(--orange)" stroke-width="2"><circle cx="12" cy="12" r="9"/><path d="M3 12h18M12 3c3 3 3 15 0 18M12 3c-3 3-3 15 0 18"/></svg></span>
      </div>
      <p class="contact">Office Number: 216-555-0143</p>
      <p class="contact">Mobile: 216-555-0192</p>
      <p class="contact">Website: www.lanternfieldhr.example</p>
      <div class="rule"></div>
      <p class="address">4827 Millbrook Ave Suite 230<br>Cleveland, Ohio 44987</p>
    </div>
  </section>

</main>
</body>
</html>
```